bluegate mental health stationary

Please help turn this logo into a total image for my business.
Stationary need to be able to be individualized for each mental health practitioners

Some generic info about services
Clinical Psychology - Consultant Psychiatry - Locum Services - Medico-legal - Architectural Adviser Clinical and Medical Facilities

Target Market(s)

Letter head for doctors, courts, patients.

Industry/Entity Type

Mental Health

Requirements
Must have
• area where practitioners details can be listed and logo on page
Nice to have
• embossed section

```html
<!DOCTYPE html>
<html lang="en">
<head>
<meta charset="utf-8">
<title>Bluegate Mental Health – Business Card</title>
<link rel="stylesheet" href="https://fonts.googleapis.com/css2?family=Belleza&family=Arimo:wght@400&display=swap">
<style>
  :root {
    --canvas-bg: #e6e6e6;
    --card-white: #ffffff;
    --blue-light: #0a89ad;
    --blue-mid: #07779c;
    --blue-deep: #0d4f6e;
    --navy: #173f5f;
    --teal-text: #1a8fb5;
    --grey-text: #555555;
    --brand-font: "Belleza", sans-serif;
    --body-font: "Arimo", Arial, sans-serif;
  }
  * { margin: 0; padding: 0; box-sizing: border-box; }
  html, body {
    width: 910px; height: 1200px; overflow: hidden;
    background: var(--canvas-bg);
  }
  .canvas { position: relative; width: 910px; height: 1200px; }

  /* Front of card */
  .card-front {
    position: absolute; left: 48px; top: 43px; width: 818px; height: 529px;
    background: radial-gradient(ellipse at 45% 40%, var(--blue-light) 0%, var(--blue-mid) 45%, var(--blue-deep) 100%);
  }
  .front-mark {
    position: absolute; left: 103px; top: 180px; width: 171px; height: 169px;
    background: var(--card-white); border-radius: 8px;
  }
  .front-name {
    position: absolute; left: 310px; top: 190px;
    font-family: var(--brand-font); font-weight: 400; color: var(--card-white);
    line-height: 1;
  }
  .front-name .name-main { display: block; font-size: 84px; letter-spacing: 1px; }
  .front-name .name-sub { display: block; font-size: 44px; margin-top: 10px; letter-spacing: 1px; }

  /* Back of card */
  .card-back {
    position: absolute; left: 46px; top: 625px; width: 818px; height: 529px;
    background: var(--card-white);
  }
  .back-mark {
    position: absolute; left: 46px; top: 39px; width: 83px; height: 83px;
    background: var(--navy); border-radius: 4px;
  }
  .back-name {
    position: absolute; left: 146px; top: 46px;
    font-family: var(--brand-font); font-weight: 400; color: var(--navy); line-height: 1;
  }
  .back-name .name-main { display: block; font-size: 42px; }
  .back-name .name-sub { display: block; font-size: 22px; margin-top: 4px; letter-spacing: 0.5px; }

  .practitioner {
    position: absolute; right: 74px; top: 144px; text-align: right;
    font-family: var(--body-font);
  }
  .practitioner-name { font-size: 21px; color: var(--teal-text); }
  .practitioner-detail { font-size: 18px; color: var(--grey-text); margin-top: 9px; line-height: 1.5; }

  .contact-list {
    position: absolute; left: 44px; top: 342px; list-style: none;
    font-family: var(--body-font); font-size: 16.5px; color: var(--grey-text);
  }
  .contact-list li { display: flex; align-items: center; height: 26px; }
  .contact-list svg { width: 24px; height: 18px; margin-right: 4px; fill: var(--teal-text); flex: none; }
  .registration {
    position: absolute; left: 29px; top: 447px;
    font-family: var(--body-font); font-size: 16px; color: var(--grey-text); line-height: 1.25;
  }
  .registration .label { color: var(--teal-text); }
  .registration .gap { display: inline-block; width: 28px; }
  .registration .web { color: var(--teal-text); display: block; }

  .card-band {
    position: absolute; left: 0; bottom: 0; width: 100%; height: 25px;
    background: linear-gradient(90deg, var(--navy) 0%, var(--blue-light) 50%, var(--navy) 100%);
  }
</style>
</head>
<body>
<div class="canvas">
  <section class="card-front">
    <div class="front-mark"></div>
    <div class="front-name">
      <span class="name-main">BLUEGATE</span>
      <span class="name-sub">MENTAL HEALTH</span>
    </div>
  </section>

  <section class="card-back">
    <div class="back-mark"></div>
    <div class="back-name">
      <span class="name-main">BLUEGATE</span>
      <span class="name-sub">MENTAL HEALTH</span>
    </div>

    <div class="practitioner">
      <p class="practitioner-name">Doctor’s Name</p>
      <p class="practitioner-detail">Qualifications<br>Description</p>
    </div>

    <ul class="contact-list">
      <li>
        <svg viewBox="0 0 24 18" aria-hidden="true"><path d="M12 1a5.5 5.5 0 0 0-5.5 5.5C6.5 10.5 12 17 12 17s5.5-6.5 5.5-10.5A5.5 5.5 0 0 0 12 1zm0 7.8a2.3 2.3 0 1 1 0-4.6 2.3 2.3 0 0 1 0 4.6z"/></svg>
        24 Harlow Street, ELMWOOD 6031
      </li>
      <li>
        <svg viewBox="0 0 24 18" aria-hidden="true"><path d="M7.5 1.5l2.6 3.3-1.6 2.2c1 2.1 2.6 3.7 4.7 4.7l2.2-1.6 3.3 2.6-1.5 3.1C10.4 15.5 5 10.1 4.2 3z"/></svg>
        (08) 9312 4480 or 0418 205 396
      </li>
      <li>
        <svg viewBox="0 0 24 18" aria-hidden="true"><path d="M9 0h6a1.5 1.5 0 0 1 1.5 1.5v15A1.5 1.5 0 0 1 15 18H9a1.5 1.5 0 0 1-1.5-1.5v-15A1.5 1.5 0 0 1 9 0zm.3 2v11h5.4V2zM12 14.3a1.2 1.2 0 1 0 0 2.4 1.2 1.2 0 0 0 0-2.4z"/></svg>
        +000 000 0000
      </li>
      <li>
        <svg viewBox="0 0 24 18" aria-hidden="true"><path d="M2 3h20v12H2zm1.8 1.4L12 10l8.2-5.6z"/></svg>
        name@bgmh.net.au
      </li>
    </ul>

    <p class="registration">
      <span class="label">ABN:</span>41 206 118 952<span class="gap"></span><span class="label">ACN:</span>208417736
      <span class="web">www.bluegatementalhealth.com</span>
    </p>

    <div class="card-band"></div>
  </section>
</div>
</body>
</html>
```